HTML Email Signature Design for Consulting Firm

We need an eamil signature design for an environmental consulting firm. The signature should be the best we can find in the market for a consulting firm in professional terms.

The design should include the following social media sites:

-Pelmosta
-Quibrel
- Gromvale

It is important that the signature is visually appealing alonside our logo.

Instructions on how to insert the signature within Microsoft Outlook are desirable as part of the deliverables.

The main reason we need HTML is that a recipient of our emails should be able to copy information from the signature and use it on the web etc..

Target Market(s)

private and public cleints

Industry/Entity Type

Environmental Consultant

Requirements
Must have
• Professional appeal ; Color combination blends nicely with Logo
Nice to have
• Blend nicely with Logo
Should not have
• No shadows in design

```html
<!DOCTYPE html>
<html lang="en">
<head>
<meta charset="utf-8">
<title>Terravolta Email Signature Banners</title>
<link rel="stylesheet" href="https://fonts.googleapis.com/css2?family=Montserrat:wght@500;600;700&display=swap">
<style>
  :root {
    --page: #ffffff;
    --ink: #363d55;
    --white: #ffffff;
    --green-start: #b0ef50;
    --green-end: #129a44;
    --cyan-start: #00f5f8;
    --cyan-end: #0a72a0;
    --sun-start: #f8fc00;
    --sun-end: #ff8700;
  }
  html, body {
    margin: 0;
    padding: 0;
    width: 1200px;
    height: 1000px;
    overflow: hidden;
    background: var(--page);
  }
  .canvas {
    position: relative;
    width: 1200px;
    height: 1000px;
  }
  .signature {
    position: absolute;
    left: 216px;
    width: 768px;
    height: 226px;
    overflow: hidden;
  }
  .signature--green { top: 67px;  background: linear-gradient(100deg, var(--green-start), var(--green-end) 75%); }
  .signature--cyan  { top: 390px; background: linear-gradient(100deg, var(--cyan-start), var(--cyan-end) 80%); }
  .signature--sun   { top: 706px; background: linear-gradient(90deg, var(--sun-start), var(--sun-end) 95%); }

  .brand-mark {
    position: absolute;
    left: 28px;
    top: 52px;
    width: 104px;
    height: 104px;
    border-radius: 50%;
    background: rgba(255, 255, 255, 0.35);
  }
  .brand-name {
    position: absolute;
    left: 145px;
    top: 84px;
    margin: 0;
    font-family: "Montserrat", sans-serif;
    font-weight: 700;
    font-size: 36px;
    line-height: 1;
    letter-spacing: 3px;
    color: var(--ink);
  }
  .brand-tagline {
    position: absolute;
    left: 146px;
    top: 120px;
    margin: 0;
    font-family: "Montserrat", sans-serif;
    font-weight: 500;
    font-size: 17px;
    line-height: 20px;
    letter-spacing: 0.3px;
    color: var(--ink);
  }
  .social-links {
    position: absolute;
    right: 20px;
    top: 176px;
    display: flex;
    gap: 22px;
    margin: 0;
    padding: 0;
    list-style: none;
  }
  .social-links li {
    display: flex;
    align-items: center;
    gap: 6px;
    font-family: "Montserrat", sans-serif;
    font-weight: 600;
    font-size: 15px;
    line-height: 20px;
    color: var(--white);
  }
  .social-links li::before {
    content: "";
    width: 11px;
    height: 11px;
    border-radius: 50%;
    background: var(--white);
  }
</style>
</head>
<body>
<main class="canvas">

  <section class="signature signature--green">
    <span class="brand-mark"></span>
    <h1 class="brand-name">TERRAVOLTA</h1>
    <p class="brand-tagline">Bridging research and public policy</p>
    <ul class="social-links">
      <li>Gromvale</li>
      <li>Quibrel</li>
      <li>Pelmosta</li>
    </ul>
  </section>

  <section class="signature signature--cyan">
    <span class="brand-mark"></span>
    <h1 class="brand-name">TERRAVOLTA</h1>
    <p class="brand-tagline">Bridging research and public policy</p>
    <ul class="social-links">
      <li>Gromvale</li>
      <li>Quibrel</li>
      <li>Pelmosta</li>
    </ul>
  </section>

  <section class="signature signature--sun">
    <span class="brand-mark"></span>
    <h1 class="brand-name">TERRAVOLTA</h1>
    <p class="brand-tagline">Bridging research and public policy</p>
    <ul class="social-links">
      <li>Gromvale</li>
      <li>Quibrel</li>
      <li>Pelmosta</li>
    </ul>
  </section>

</main>
</body>
</html>
```